1 Simple Menu Board Design For Ice Cream Shop

We are a shaved ice shop that needs ONE menu board designed with 6 pre-set shaved ice combinations. This is a very simple project where I will give you all the images and text you need for the menu board.

Requirements:
1) I need the photoshop or illustrator file after you are finished (in case we need to make minor tweaks in the future). If you win, I will give you a site for you to ftp the final photoshop or illustrator file. (Adobe Photoshop or Illustrator only!)
2) Menu board design dimensions must be 9,600 pixels height x 5,400 pixels wide (want it large so can print on large posters if needed in the future)
3) Design must "fit" with our existing menu board designs, but of course look professional. But do NOT be bound by our previous menu boards. If you have a BETTER more exciting/stylish/classy design in your head, go for it.
4) The 6 ice combos should FILL up the entire menu board. Don't want too much "empty" background space around pictures. The ICE should be stars of the board. Please take a look at "[login to view URL]" for format we would like the menu board to look.
5) Please use the [login to view URL] file as the background file for this menu board. But only use right half side.
**** UPDATE: PLEASE TAKE A LOOK AT "[login to view URL]" for what we hope the ice combo menu board to look like. Please tastefully crop the ice pics to fit into the boxes. The titles ie: "1 Vanilla Milk" should be placed under the picture of the ice.

Design Criteria:

- Top of menu board should say "Popular Ice Combos" in a classy way. Please don't tweak text into wavy shapes, or other cheesy shapes. Do NOT write the title "vela ice" or any other title on this menu board besides "Popular Ice Combos".
- 6 combos on menu board. 3 Rows x 2 columns of combos each should FILL UP menu board. DON'T rotate the 6 boxes.
- When scaled, Text size should be approximately same size as the text in Vela2-Menu1 file.
- Probably best if ice pictures cropped out, and if needed black backgrounds replaced with a tasteful "blurred" background
- A clear cropped picture of each ice combo with the name of the combo (larger font), and under the combo name, a description of what is included in the combo (smaller font) should be included.
- Each ice combo needs the NUMBER written somewhere so people can call the combo by number (1,2..6) Don't just write "Vanilla Milk". etc..
- Ice descriptions/Toppings should be all in lower case
- Layout of ice on board should look like the following:
#1 #2
#3 #4
#5 #6

These are the combos and descriptions:
#1 Vanilla Milk (strawberries, crunkets, condensed milk, chocolate drizzle)
#2 Green Tea (flan pudding, red bean, condensed milk)
#3 Sea Salt Caramel (almond slices, crunkets, caramel drizzle)
#4 Strawberry (boba, strawberry jelly, Strawberry drizzle)
#5 Chocolate (b&ts, marshmallows, chocolate drizzle)
#6 Coconut (rainbow jelly, mango poppers, mango drizzle)

Will be Given:
Attached are the 6 images of the combinations, which you will need to crop and fit on the menu board. Preferably don't use the dark black background colors from the photos of the ice, as the black colors don't seem to fit with the other menu board feel. A tasteful "blurred" background can be used to fill up empty space behind ice if needed for each square. Again, This menu board I need you to design will be on the right half of the file [login to view URL], and must blend well wight the left half image.

Also attached are other menu boards that we currently have and the feel we want the menu board to blend with.

Please submit your design on top of the file "[login to view URL]", where I can see the existing left side design, and your new right side combo design.

```html
<!DOCTYPE html>
<html lang="en">
<head>
<meta charset="utf-8">
<title>Vela Ice Menu Board</title>
<link rel="stylesheet" href="https://fonts.googleapis.com/css2?family=Arimo:wght@400;700&family=Lobster&family=Chewy&display=swap">
<style>
  :root{
    --sky-top:#bfe6f7;
    --sky-bottom:#e6f6fc;
    --panel-left:#d7eff9;
    --panel-right:#3d8fe0;
    --panel-right-dark:#2f7bd0;
    --brand-blue:#1c6fb8;
    --flavor-blue:#1a73c2;
    --ink:#111;
    --magenta:#e0127f;
    --pink-title:#e8157c;
    --white:#ffffff;
  }
  *{margin:0;padding:0;box-sizing:border-box}
  html,body{width:1200px;height:1067px;overflow:hidden}
  body{
    background:linear-gradient(180deg,var(--sky-top),var(--sky-bottom));
    font-family:"Arimo",Arial,sans-serif;
    position:relative;
  }
  .board{position:absolute;inset:0}

  /* left panel */
  .menu-panel{
    position:absolute;left:33px;top:33px;width:563px;height:1007px;
    background:linear-gradient(180deg,#e4f5fc,var(--panel-left));
  }
  .brand-name{
    position:absolute;left:30px;top:30px;
    font-family:"Arimo",Arial,sans-serif;font-weight:700;font-size:104px;
    letter-spacing:-2px;color:var(--brand-blue);line-height:1;
  }
  .brand-tagline{
    position:absolute;left:100px;top:158px;
    font-size:29px;color:var(--brand-blue);
  }
  .sizes{position:absolute;left:40px;top:222px;font-size:24px;color:var(--ink);line-height:32px}
  .sizes .row{display:flex}
  .sizes .label{width:217px;white-space:nowrap}
  .sizes .indent{padding-left:98px;width:217px;white-space:nowrap}
  .sizes .price{color:var(--magenta)}

  .customize-badge{
    position:absolute;left:380px;top:196px;width:140px;height:140px;border-radius:50%;
    background:var(--magenta);border:5px solid var(--white);
    box-shadow:0 2px 6px rgba(0,0,0,.25);
    display:flex;align-items:center;justify-content:center;text-align:center;
  }
  .customize-badge span{
    font-family:"Chewy","Arial Black",Arial,sans-serif;font-weight:700;color:var(--white);
    font-size:20px;line-height:24px;white-space:nowrap;
    transform:rotate(-10deg);
  }

  .flavors-heading{position:absolute;left:40px;top:302px;font-size:24px;font-weight:700;color:var(--ink)}
  .flavor-list{
    position:absolute;left:40px;top:332px;width:460px;
    display:grid;grid-template-columns:238px 222px;grid-auto-rows:29px;
    font-size:24px;color:var(--flavor-blue);list-style:none;white-space:nowrap;
  }
  .star{color:var(--magenta)}
  .fruit-note{position:absolute;left:40px;top:537px;font-size:17px;color:var(--ink)}
  .pick-line{position:absolute;left:40px;top:564px;font-size:24px;color:var(--ink)}
  .pick-line b{font-weight:700}

  .order-arrow{position:absolute;top:615px;width:84px;height:86px}
  .order-arrow.left{left:-12px}
  .order-arrow.right{left:464px}
  .order-button{
    position:absolute;left:80px;top:606px;width:374px;height:52px;border-radius:26px;
    background:var(--magenta);border:4px solid var(--white);
    box-shadow:0 2px 5px rgba(0,0,0,.3);
    display:flex;align-items:center;justify-content:center;
    font-family:"Chewy","Arial Black",Arial,sans-serif;font-weight:700;
    font-size:18px;color:var(--white);white-space:nowrap;
  }
  .feature-photo{position:absolute;border-radius:14px}
  .feature-photo.green{left:-20px;top:690px;width:310px;height:300px;
    background:radial-gradient(ellipse at 45% 45%,#9bb36a 0,#8aa25a 45%,#e35b4f 75%,rgba(240,160,80,0) 100%)}
  .feature-photo.vanilla{left:270px;top:680px;width:300px;height:290px;
    background:radial-gradient(ellipse at 50% 45%,#efe4d0 0,#e6d6bc 50%,#3a2b28 78%,rgba(255,255,255,0) 100%)}

  /* right panel */
  .combo-panel{
    position:absolute;left:596px;top:33px;width:577px;height:1007px;
    background:linear-gradient(180deg,var(--panel-right),var(--panel-right-dark));
  }
  .combo-title{
    position:absolute;left:0;right:0;top:8px;text-align:center;
    font-family:"Lobster",cursive;font-size:52px;color:var(--pink-title);
  }
  .combo-grid{
    position:absolute;left:19px;top:71px;width:548px;
    display:grid;grid-template-columns:269px 266px;column-gap:17px;grid-auto-rows:300px;
  }
  .combo{position:relative}
  .combo-photo{width:100%;height:240px}
  .combo-caption{position:relative;height:56px;color:var(--white);text-align:center}
  .combo-number{position:absolute;left:10px;top:4px;font-size:18px;font-weight:700}
  .combo-name{font-family:"Lobster",cursive;font-size:23px;color:var(--pink-title);line-height:30px;padding-top:2px}
  .combo-toppings{font-size:13px;line-height:16px;white-space:nowrap}

  .p1{background:linear-gradient(180deg,#7fc6ea,#e9e4dc 45%,#c4301e 92%)}
  .p2{background:linear-gradient(180deg,#7fc6ea,#7e9f4c 40%,#5b2a1a 92%)}
  .p3{background:linear-gradient(180deg,#7fc6ea,#e8d6b4 45%,#2a211c 92%)}
  .p4{background:linear-gradient(180deg,#7fc6ea,#ef9aa6 45%,#b8202a 92%)}
  .p5{background:linear-gradient(180deg,#7fc6ea,#6b4a34 45%,#d9d2c6 92%)}
  .p6{background:linear-gradient(180deg,#7fc6ea,#f4e6b0 45%,#f0a41e 92%)}
</style>
</head>
<body>
<main class="board">

  <section class="menu-panel">
    <h1 class="brand-name">vela ice</h1>
    <p class="brand-tagline">Artisan Shaved Ice</p>

    <div class="sizes">
      <div class="row"><span class="label">Sizes: Hill</span><span class="price">5</span></div>
      <div class="row"><span class="indent">Mountain</span><span class="price">7</span></div>
    </div>

    <div class="customize-badge"><span>CUSTOMIZE<br>YOUR ICE</span></div>

    <h2 class="flavors-heading">Ice Flavors:</h2>
    <ul class="flavor-list">
      <li>Vanilla Milk</li><li></li>
      <li>Green Tea</li><li>Sea Salt Caramel</li>
      <li>Coffee</li><li>Almond</li>
      <li>Chocolate</li><li>Peanut Butter</li>
      <li>Strawberry <span class="star">✻</span></li><li>Mango <span class="star">✻</span></li>
      <li>Coconut <span class="star">✻</span></li><li>Durian <span class="star">✻</span></li>
      <li>Taro <span class="star">✻</span></li><li>Lychee <span class="star">✻</span></li>
    </ul>
    <p class="fruit-note"><span class="star">✻</span> = fruit ice additional 0.50(H) / 0.75(M)</p>
    <p class="pick-line">Pick Your <b>Toppings</b> and <b>Drizzle</b></p>

    <svg class="order-arrow left" viewBox="0 0 84 86" aria-hidden="true">
      <path d="M22 4h40v38h18L42 82 4 42h18z" fill="#b8327a" stroke="#fff" stroke-width="3"/>
    </svg>
    <div class="order-button">GET YOUR ICE ORDER FORM BELOW</div>
    <svg class="order-arrow right" viewBox="0 0 84 86" aria-hidden="true">
      <path d="M22 4h40v38h18L42 82 4 42h18z" fill="#b8327a" stroke="#fff" stroke-width="3"/>
    </svg>

    <div class="feature-photo green" role="img" aria-label="Photo of green tea shaved ice with strawberries and mango cubes"></div>
    <div class="feature-photo vanilla" role="img" aria-label="Photo of vanilla milk shaved ice with boba pearls"></div>
  </section>

  <section class="combo-panel">
    <h2 class="combo-title">Popular Ice Combos</h2>
    <div class="combo-grid">
      <article class="combo">
        <div class="combo-photo p1" role="img" aria-label="Photo of vanilla milk shaved ice with strawberries and chocolate drizzle"></div>
        <div class="combo-caption"><span class="combo-number">1</span><h3 class="combo-name">Vanilla Milk</h3><p class="combo-toppings">Strawberry, Crunkets, Chocolate drizzle</p></div>
      </article>
      <article class="combo">
        <div class="combo-photo p2" role="img" aria-label="Photo of green tea shaved ice with flan pudding and red bean"></div>
        <div class="combo-caption"><span class="combo-number">2</span><h3 class="combo-name">Green Tea</h3><p class="combo-toppings">Flan pudding, Red bean, Condensed milk</p></div>
      </article>
      <article class="combo">
        <div class="combo-photo p3" role="img" aria-label="Photo of sea salt caramel shaved ice with almond slices"></div>
        <div class="combo-caption"><span class="combo-number">3</span><h3 class="combo-name">Sea Salt Caramel</h3><p class="combo-toppings">Almond slices, Crunkets, Caramel drizzle</p></div>
      </article>
      <article class="combo">
        <div class="combo-photo p4" role="img" aria-label="Photo of strawberry shaved ice with boba and strawberry jelly"></div>
        <div class="combo-caption"><span class="combo-number">4</span><h3 class="combo-name">Strawberry</h3><p class="combo-toppings">Boba, Strawberry jelly, Strwberry drizzle</p></div>
      </article>
      <article class="combo">
        <div class="combo-photo p5" role="img" aria-label="Photo of chocolate shaved ice with candies and marshmallows"></div>
        <div class="combo-caption"><span class="combo-number">5</span><h3 class="combo-name">Chocolate</h3><p class="combo-toppings">B&amp;Ts, Marshmallows, Chocolate drizzle</p></div>
      </article>
      <article class="combo">
        <div class="combo-photo p6" role="img" aria-label="Photo of coconut shaved ice with mango poppers and mango jelly"></div>
        <div class="combo-caption"><span class="combo-number">6</span><h3 class="combo-name">Coconut</h3><p class="combo-toppings">Mango poppers, Mango jelly, Rainbow jelly</p></div>
      </article>
    </div>
  </section>

</main>
</body>
</html>
```